Web page for Gareth Pemblewick Chartered Tax Adviser

I need to take the basic web page that I have created and "Brand it" to be compatible with the corporate logo and stationery created for me by other Studio Flock designers.
I will need a watermark as well as a distinctive home page and then a branded general page for content including a series of Blogs.

Target Market(s)

My practice deals with expatriates including those looking to invest in Australia.

Industry/Entity Type

Crowd

Font styles to use
Other font styles liked:
• Per logo

Requirements
Must have
• Besides the homepage I will need a general page for content, branded in the same style as the letterheads.
Nice to have
• A watermark to go with the blogs and news content.

```html
<!DOCTYPE html>
<html lang="en">
<head>
<meta charset="utf-8">
<title>Gareth Pemblewick — Chartered Tax Adviser</title>
<link href="https://fonts.googleapis.com/css2?family=Lato:ital,wght@0,400;0,700;0,900;1,400&display=swap" rel="stylesheet">
<style>
:root{
  --navy:#1d4e6e;
  --navy-dark:#0f3a57;
  --teal:#2b6f93;
  --ink:#222;
  --muted:#555;
  --rule:#d6d6d6;
  --band:#f3f3f3;
  --white:#fff;
}
*{box-sizing:border-box;margin:0;padding:0}
html,body{width:740px;height:1200px;overflow:hidden;background:var(--white)}
body{font-family:'Lato',sans-serif;color:var(--ink)}
.page{position:relative;width:740px;height:1200px;overflow:hidden;background:var(--white)}
.abs{position:absolute}

/* header */
.brand{left:86px;top:20px;display:flex;align-items:center;gap:10px}
.brand-mark{width:40px;height:40px;background:var(--navy);border-radius:50%}
.brand-name{font-weight:700;color:var(--navy);font-size:22px;line-height:1.05;letter-spacing:.5px}
.brand-name small{display:block;font-size:10px;letter-spacing:3px;margin-top:3px}
.phone-tab{left:534px;top:0;width:132px;height:24px;background:var(--navy);border-radius:0 0 14px 14px;color:var(--white);font-size:13px;font-weight:700;display:flex;align-items:center;justify-content:center;gap:6px}
.follow{left:560px;top:36px;font-size:9px;font-weight:700;color:var(--ink);letter-spacing:.5px}
.social{display:flex;gap:4px}
.social span{width:16px;height:16px;border-radius:50%;display:block}
.social-head{left:563px;top:50px}
.social-head span:nth-child(1){background:#3b5a9a}
.social-head span:nth-child(2){background:#2fa8e0}
.social-head span:nth-child(3){background:#1f7bb6}
.social-head span:nth-child(4){background:#ef8a22}

.nav{left:0;top:82px;width:740px;height:28px;background:linear-gradient(#3f6f8e,#1a4a69);display:flex;align-items:center}
.nav a{position:absolute;color:var(--white);text-decoration:none;font-size:9.5px;font-weight:700;letter-spacing:.3px;top:8px}
.nav .active{background:linear-gradient(#9aa3aa,#6a747c);padding:5px 10px;top:3px;border-radius:2px}
.nav .mail{font-weight:400;font-size:9.5px;display:flex;align-items:center;gap:6px}

/* hero */
.hero{left:0;top:110px;width:740px;height:324px;background:linear-gradient(100deg,#c9dbe8 0%,#8fb0c8 35%,#5d7f9a 60%,#8eaac2 80%,#bcd0df 100%)}
.hero-arrow{top:152px;width:36px;height:36px;border-radius:50%;background:rgba(255,255,255,.3);border:1px solid rgba(255,255,255,.6)}
.hero-card{left:84px;top:178px;width:220px;height:98px;background:rgba(255,255,255,.35);border-radius:4px;padding:12px 11px}
.hero-card h1{font-size:22px;font-weight:900;line-height:1.05;color:#111}
.btn{display:inline-block;background:var(--navy);color:var(--white);font-size:11px;font-weight:700;padding:6px 10px;border-radius:3px;margin-top:10px}

/* welcome */
.welcome-title{left:0;top:458px;width:740px;display:flex;justify-content:center;align-items:center;gap:8px;font-size:17px}
.welcome-title i{width:20px;height:20px;border-radius:50%;background:var(--navy)}
.welcome-title b{font-weight:700;color:var(--navy)}
.short-rule{height:1px;background:#999;width:56px}
.welcome-text{left:90px;top:496px;width:560px;text-align:center;font-size:8.4px;line-height:1.65;color:var(--muted)}
.link-more{font-size:8.5px;font-weight:700;color:var(--navy);letter-spacing:.3px}

/* services */
.services{left:0;top:580px;width:740px;height:174px;background:var(--band)}
.section-title{font-size:14px;font-weight:700;color:var(--ink)}
.section-title em{font-style:normal;color:var(--teal)}
.service{width:90px;text-align:center;top:86px}
.service-icon{width:46px;height:46px;border-radius:50%;border:2px solid var(--navy);margin:0 auto;display:flex;align-items:center;justify-content:center;position:relative}
.service-icon::after{content:"";position:absolute;inset:3px;border-radius:50%;background:var(--teal)}
.service-icon svg{position:relative;z-index:1}
.service p{font-size:7.8px;font-weight:700;line-height:1.3;margin-top:5px}

/* three columns */
.col{top:770px}
.col h2{font-size:13px;font-weight:700}
.col h2 em{font-style:normal;color:var(--teal)}
.col-rule{height:1px;background:var(--rule);margin-top:5px;position:relative}
.col-rule::before{content:"";position:absolute;left:0;top:-1px;width:40px;height:2px;background:#888}
.why li{list-style:none;display:flex;gap:8px;font-size:7.8px;line-height:1.4;color:var(--muted);padding:7px 0;border-bottom:1px dotted #ccc}
.why li i{flex:none;width:10px;height:11px;background:#aaa;border-radius:2px;margin-top:2px}
.news-item{display:flex;gap:9px;padding:7px 0;border-bottom:1px dotted #ccc}
.date{flex:none;width:30px;text-align:center}
.date b{display:block;background:var(--navy);color:var(--white);font-size:12px;padding:2px 0}
.date span{display:block;background:#eee;font-size:8px;font-weight:700;padding:2px 0;border-bottom:2px solid var(--navy)}
.news-item h3,.post h3{font-size:8.2px;font-weight:700;color:var(--ink)}
.news-item p,.post p{font-size:7.8px;line-height:1.35;color:var(--muted)}
.arrows{position:absolute;right:0;top:2px;color:#999;font-size:12px;letter-spacing:4px}
.quote{margin-top:10px;background:#eeeeee;border-radius:4px;padding:9px 10px 14px 16px;font-size:7.7px;font-style:italic;line-height:1.5;color:var(--muted);height:100px}
.avatar{width:46px;height:46px;border-radius:50%;background:linear-gradient(#cfd6dc,#6f7e8a);border:2px solid var(--white)}
.client{font-size:7.5px;font-weight:700;color:var(--teal);margin-top:6px;margin-left:10px}

/* blog */
.blog-rule{left:82px;top:962px;width:578px;height:1px;background:#eee}
.blog-title{left:0;top:982px;width:740px;text-align:center;font-size:17px;color:var(--teal)}
.blog-title span{color:#bbb;font-size:14px;margin:0 50px}
.post{top:1022px;width:175px;display:flex;gap:8px}
.post-photo{flex:none;width:40px;height:40px;background:linear-gradient(#c89f83,#6b4a3a)}
.post small{font-size:7px;font-style:italic;color:var(--muted)}
.post h3{color:var(--teal)}

/* footer */
.footer{left:0;top:1080px;width:740px;height:120px}
.foot-mark{left:94px;top:1126px;width:24px;height:24px;background:#3d6a88;border-radius:50%}
.foot-links{left:86px;top:1160px;font-size:7.6px;color:var(--white)}
.foot-copy{left:86px;top:1176px;font-size:7.6px;color:var(--white)}
.social-foot{left:562px;top:1168px}
.social-foot span{width:18px;height:18px;background:#d8d8d8;margin-right:4px}
</style>
</head>
<body>
<div class="page">

  <!-- header -->
  <div class="abs brand">
    <span class="brand-mark"></span>
    <div class="brand-name">Gareth Pemblewick<small>CHARTERED TAX ADVISER</small></div>
  </div>
  <div class="abs phone-tab">
    <svg width="11" height="11" viewBox="0 0 24 24"><path fill="#fff" d="M6.6 10.8a15 15 0 0 0 6.6 6.6l2.2-2.2c.3-.3.7-.4 1-.2 1.1.4 2.3.6 3.6.6.6 0 1 .4 1 1V20c0 .6-.4 1-1 1A17 17 0 0 1 3 4c0-.6.4-1 1-1h3.5c.6 0 1 .4 1 1 0 1.3.2 2.5.6 3.6.1.3 0 .7-.2 1z"/></svg>
    123-555-0147
  </div>
  <div class="abs follow">FOLLOW US :</div>
  <div class="abs social social-head" aria-label="Social links"><span></span><span></span><span></span><span></span></div>

  <nav class="abs nav">
    <a class="active" style="left:88px">HOME</a>
    <a style="left:150px">SERVICES</a>
    <a style="left:216px">NEWS</a>
    <a style="left:268px">BLOG</a>
    <a style="left:318px">ABOUT US</a>
    <a style="left:384px">CAREERS</a>
    <a style="left:448px">CONTACT US</a>
    <a class="mail" style="left:548px">
      <svg width="12" height="9" viewBox="0 0 12 9"><rect width="12" height="9" fill="#fff"/><path d="M0 0l6 5 6-5" stroke="#1a4a69" fill="none"/></svg>
      info@gptaxadvisors.com</a>
  </nav>

  <!-- hero -->
  <section class="abs hero" role="img" aria-label="Businessman in a suit standing by a laptop in a bright office overlooking city towers">
    <div class="abs hero-arrow" style="left:36px"><svg width="36" height="36"><path d="M20 11l-7 7 7 7" stroke="#fff" stroke-width="2" fill="none"/></svg></div>
    <div class="abs hero-arrow" style="left:668px"><svg width="36" height="36"><path d="M16 11l7 7-7 7" stroke="#fff" stroke-width="2" fill="none"/></svg></div>
    <div class="abs hero-card">
      <h1>A CENTURY OF<br>GLOBAL SERVICES</h1>
      <span class="btn">READ MORE</span>
    </div>
  </section>

  <!-- welcome -->
  <div class="abs welcome-title"><i></i>Welcome to <b>Gareth Pemblewick</b></div>
  <div class="abs short-rule" style="left:342px;top:488px"></div>
  <div class="abs welcome-text">
    Lorem ipsum dolor sit amet, consectetuer adipiscing elit, sed diam nonummy nibh euismod tincidunt ut laoreet dolore magna aliquam erat volutpat. Ut wisi enim ad minim venia m, quis nostrud exerci in amet ullamcorper suscipit lobortis nisl ut aliquip ex ea comsed diam nonummy nibh euism od tincidunt uopre laoreet dolore magna aliquam erat volutpat. lutpat. Ut wisi enim ad minim venia m, qusfis nostrud exerc.
    <div class="link-more" style="margin-top:6px">READ MORE</div>
  </div>

  <!-- services -->
  <section class="abs services">
    <div class="abs section-title" style="left:0;top:24px;width:740px;text-align:center">Our <em>Services</em></div>
    <div class="abs" style="left:86px;top:44px;width:568px;height:1px;background:var(--rule)"></div>

    <div class="abs service" style="left:75px"><div class="service-icon"><svg width="20" height="20" viewBox="0 0 20 20"><rect x="5" y="3" width="10" height="14" fill="none" stroke="#fff" stroke-width="1.6"/><path d="M7 7h6M7 10h6M7 13h4" stroke="#fff"/></svg></div><p>AUDIT &amp;<br>ASSURANCE</p></div>
    <div class="abs service" style="left:158px"><div class="service-icon"><svg width="20" height="20" viewBox="0 0 20 20"><rect x="4" y="3" width="11" height="14" fill="none" stroke="#fff" stroke-width="1.6"/><path d="M7 10l2 2 5-5" stroke="#fff" stroke-width="1.6" fill="none"/></svg></div><p>BUSINESS<br>ADVISORY</p></div>
    <div class="abs service" style="left:239px"><div class="service-icon"><svg width="20" height="20" viewBox="0 0 20 20"><circle cx="10" cy="10" r="7" fill="#fff"/><path d="M10 10V3a7 7 0 0 1 7 7z" fill="#2b6f93" stroke="#fff"/></svg></div><p>OUR<br>TAXATION</p></div>
    <div class="abs service" style="left:322px"><div class="service-icon"><svg width="20" height="20" viewBox="0 0 20 20"><rect x="3" y="7" width="14" height="9" rx="1" fill="#fff"/><rect x="7" y="4" width="6" height="3" fill="none" stroke="#fff" stroke-width="1.4"/></svg></div><p>BUSINESS RECOVERY<br>AND INSOLVENCY</p></div>
    <div class="abs service" style="left:405px"><div class="service-icon"><svg width="20" height="20" viewBox="0 0 20 20"><path d="M3 11l5-5 4 4-5 5zM17 11l-5-5-4 4 5 5z" fill="#fff"/></svg></div><p>CORPORATE<br>FINANCE</p></div>
    <div class="abs service" style="left:488px"><div class="service-icon"><svg width="20" height="20" viewBox="0 0 20 20"><circle cx="10" cy="12" r="6" fill="#fff"/><path d="M8 3h4l-1 3H9z" fill="#fff"/></svg></div><p>WEALTH<br>CREATION</p></div>
    <div class="abs service" style="left:572px"><div class="service-icon"><svg width="20" height="20" viewBox="0 0 20 20"><path d="M3 17V9l4 3V9l4 3V9l4 3V4h2v13z" fill="#fff"/></svg></div><p>INDUSTRY<br>SECTORS</p></div>
  </section>

  <!-- why choose us -->
  <section class="abs col why" style="left:82px;width:176px">
    <h2>Why <em>Choose Us</em></h2>
    <div class="col-rule"></div>
    <ul style="margin-top:4px">
      <li><i></i>Lorem ipsum dolor sit tetu adipiscing elised diam nonummy nibh euismod</li>
      <li><i></i>Lorem ipsum dolor sit tetu adipiscing elised diam nonummy nibh euismod</li>
      <li><i></i>Lorem ipsum dolor sit tetu adipiscing elised</li>
      <li><i></i>Ktu adipiscing elitsied orem ipsum dolor sit</li>
      <li style="border:none"><i></i>Ktu adipiscing elitsied orem ipsum dolor sit</li>
    </ul>
  </section>

  <!-- latest news -->
  <section class="abs col" style="left:283px;width:177px">
    <h2>Latest <em>News</em></h2>
    <span class="arrows">‹ ›</span>
    <div class="col-rule"></div>
    <div class="news-item"><div class="date"><b>30</b><span>DEC</span></div><div><h3>Lorem ipsum dolor sit ametcons...</h3><p>Sed diam nonmy nibh eumod tincidun ut laoreet dolore magna aliquam.</p></div></div>
    <div class="news-item"><div class="date"><b>20</b><span>DEC</span></div><div><h3>Lorem ipsum dolor sit ametcons...</h3><p>Sed diam nonmy nibh eumod tincidun ut laoreet dolore magna aliquam.</p></div></div>
    <div class="news-item" style="border:none"><div class="date"><b>10</b><span>DEC</span></div><div><h3>Lorem ipsum dolor sit ametcons...</h3><p>Sed diam nonmy nibh eumod tincidun ut laoreet dolore magna aliquam.</p></div></div>
  </section>

  <!-- testimonials -->
  <section class="abs col" style="left:485px;width:175px">
    <h2>Client <em>Testimonials</em></h2>
    <span class="arrows">‹ ›</span>
    <div class="col-rule"></div>
    <div class="quote">Lorem ipsum dolor sit amet consctueropf adipiscing elit, sed diam nonmy nibh euismodg tincidunt ut laoreet dolore magna aliquam eratg volutpat. ut wisi enim ad minim veniam, quis nostrud exerci tation ullamcorper suscipit tation ulicorper suscipit tation.</div>
    <div class="abs avatar" role="img" aria-label="Client portrait" style="left:118px;top:118px"></div>
    <div class="client">MR. ALDEN CREWE</div>
  </section>

  <!-- blog -->
  <div class="abs blog-rule"></div>
  <div class="abs blog-title"><span>‹</span>Recent Blog Posts<span>›</span></div>
  <article class="abs post" style="left:84px"><div class="post-photo" role="img" aria-label="Author portrait"></div><div><small>Posted on 30 Dec, 2014</small><h3>Lorem ipsum dolor sit ametcons...</h3><p>Sed diam nonmy nibh eumod tincidun ut laoreet dolore magna aliquam.</p></div></article>
  <article class="abs post" style="left:285px"><div class="post-photo" role="img" aria-label="Author portrait"></div><div><small>Posted on 30 Dec, 2014</small><h3>Lorem ipsum dolor sit ...</h3><p>Sed diam nonmy nibh eumod tinc dun ut laoreet dolore a aliam.</p></div></article>
  <article class="abs post" style="left:473px"><div class="post-photo" role="img" aria-label="Author portrait"></div><div><small>Posted on 30 Dec, 2014</small><h3>Lorem ipsum dolor sit ametcons...</h3><p>Sed diam nonmy nibh eumod tincidun ut laoreet dolore magna aliquam.</p></div></article>

  <!-- footer -->
  <svg class="abs footer" viewBox="0 0 740 120" preserveAspectRatio="none">
    <defs><linearGradient id="footGrad" x1="0" x2="1"><stop offset="0" stop-color="#1c5677"/><stop offset="1" stop-color="#0d2f4d"/></linearGradient></defs>
    <path d="M0 40 C180 -10 500 0 740 30 L740 120 L0 120Z" fill="#b9bcbf"/>
    <path d="M0 52 C180 5 500 16 740 40 L740 120 L0 120Z" fill="url(#footGrad)"/>
  </svg>
  <div class="abs foot-mark"></div>
  <div class="abs foot-links">Home &nbsp;|&nbsp; Services &nbsp;|&nbsp; News &nbsp;|&nbsp; Blog &nbsp;|&nbsp; About Us &nbsp;|&nbsp; Careers &nbsp;|&nbsp; Contact Us &nbsp;|&nbsp; Privacy Policy</div>
  <div class="abs foot-copy">© 2014 <b>GPTaxadvisors</b>. All Right Reserved.</div>
  <div class="abs social social-foot" aria-label="Social links"><span></span><span></span><span></span><span></span></div>

</div>
</body>
</html>
```